Digital & Print Graphic Design templates for Comedy Club

We need new new digital & print graphic design templates for our upcoming comedy events created for use in CANVA in the following specs
Digital:
1080x1080px
1200x600px
800x400px
1920x1080px
1080x1355px
1500x500px
851x315px
Print
11x17"
22x28"
95.5x30"

Target Market(s)

18+ comedy fans

Industry/Entity Type

comedy club

Font styles to use
Sans Serif

Colors
FFF300
FFF600
FEFA6F
FFFEC7
FFFEE8
6B429C
8869AF
B7A5CE
E3DAEB
F3F0F8

Requirements
Must have
• templates must be CANVA compatible. frame for comedian photo.
Nice to have
• would like to incorporate deep purple into the design
Should not have
• do not include phone number on any templates

```html
<!DOCTYPE html>
<html lang="en">
<head>
<meta charset="UTF-8">
<title>Sam Carver – The Giggle Room</title>
<link rel="stylesheet" href="https://fonts.googleapis.com/css2?family=Poppins:wght@300;600;700;800&family=Sacramento&display=swap">
<style>
  :root {
    --yellow: #FFF300;
    --yellow-glow: #FEFA6F;
    --cream: #FFFEE8;
    --white: #FFFFFF;
    --ink: #111111;
    --bg-top: #8e8f8f;
    --bg-mid: #6f7166;
    --bg-bottom: #121316;
    --suit-light: #2f6f96;
    --suit-dark: #123049;
  }
  * { margin: 0; padding: 0; box-sizing: border-box; }
  html, body { width: 675px; height: 1200px; overflow: hidden; background: var(--bg-bottom); }
  .poster {
    position: relative;
    width: 675px;
    height: 1200px;
    overflow: hidden;
    font-family: "Poppins", sans-serif;
    background: linear-gradient(180deg, var(--bg-top) 0%, #858680 45%, var(--bg-mid) 65%, var(--bg-bottom) 100%);
  }
  .comedian-photo {
    position: absolute;
    left: 30px;
    top: 300px;
    width: 580px;
    height: 900px;
    border-radius: 120px 120px 0 0;
    background: linear-gradient(180deg, rgba(47,111,150,0.0) 0%, var(--suit-light) 18%, #1f5577 55%, var(--suit-dark) 82%, #0c1520 100%);
  }
  .shade {
    position: absolute;
    left: 0; right: 0; bottom: 0;
    height: 420px;
    background: linear-gradient(180deg, transparent 0%, rgba(10,10,12,0.75) 100%);
  }
  .brand {
    position: absolute;
    left: 60px;
    top: 56px;
    width: 150px;
    height: 150px;
    display: flex;
    flex-direction: column;
    align-items: center;
    justify-content: center;
    gap: 8px;
  }
  .brand-dot {
    width: 22px;
    height: 22px;
    border-radius: 50%;
    background: var(--yellow);
  }
  .brand-name {
    font-weight: 700;
    font-size: 20px;
    line-height: 1.1;
    text-align: center;
    color: var(--yellow);
  }
  .dates {
    position: absolute;
    right: 69px;
    top: 76px;
    text-align: right;
    color: var(--white);
  }
  .dates-month { font-weight: 700; font-size: 20px; letter-spacing: -0.5px; line-height: 1; }
  .dates-days { font-weight: 300; font-size: 36px; line-height: 1.1; margin-top: 4px; }
  .event-tag {
    position: absolute;
    left: 53px;
    top: 237px;
    height: 102px;
    border-left: 2px solid var(--white);
    padding-left: 22px;
    padding-top: 6px;
    color: var(--white);
    font-weight: 600;
    font-size: 23px;
    line-height: 30px;
    letter-spacing: 2.5px;
  }
  .headliner {
    position: absolute;
    left: 0;
    right: 0;
    top: 535px;
    text-align: center;
    font-family: "Poppins", sans-serif;
    font-weight: 800;
    font-size: 124px;
    line-height: 165px;
    letter-spacing: 2px;
    color: var(--cream);
    text-shadow: 0 0 10px var(--yellow-glow), 0 0 24px rgba(255,243,0,0.7), 0 0 44px rgba(255,243,0,0.45);
  }
  .tagline {
    position: absolute;
    left: 180px;
    top: 885px;
    font-family: "Sacramento", cursive;
    font-size: 68px;
    color: var(--cream);
    transform: rotate(-7deg);
    text-shadow: 0 0 6px var(--yellow), 0 0 16px rgba(255,243,0,0.8);
  }
  .cta {
    position: absolute;
    left: 222px;
    top: 1047px;
    width: 231px;
    height: 41px;
    background: var(--yellow);
    color: var(--ink);
    font-weight: 700;
    font-size: 17px;
    letter-spacing: 2px;
    display: flex;
    align-items: center;
    justify-content: center;
  }
  .website {
    position: absolute;
    left: 0;
    right: 0;
    top: 1098px;
    text-align: center;
    color: var(--white);
    font-weight: 700;
    font-size: 24px;
    letter-spacing: 1.5px;
  }
</style>
</head>
<body>
  <main class="poster">
    <div class="comedian-photo" role="img" aria-label="Photo of the comedian in a blue suit and white shirt holding a microphone on stage"></div>
    <div class="shade"></div>

    <div class="brand">
      <span class="brand-dot"></span>
      <span class="brand-name">The Giggle Room</span>
    </div>

    <div class="dates">
      <div class="dates-month">APRIL</div>
      <div class="dates-days">16-18</div>
    </div>

    <div class="event-tag">EXCLUSIVE<br>CONCERT<br>EVENT</div>

    <h1 class="headliner">SAM<br>CARVER</h1>
    <div class="tagline">Enjoy the show</div>

    <div class="cta">REGISTER NOW</div>
    <div class="website">www.giggleroomyyc.com</div>
  </main>
</body>
</html>
```